Marrowfield Contracting Business Cards

Front of card:

Full Logo
Name
Address
Office Phone
Cell Phone
Email
Website

Back:
Logo Mark in background
List and markets and services performed

```html
<!DOCTYPE html>
<html lang="en">
<head>
<meta charset="utf-8">
<title>Marrowfield Contracting Business Cards</title>
<link href="https://fonts.googleapis.com/css2?family=Mulish:wght@400;700;800&display=swap" rel="stylesheet">
<style>
  :root {
    --backdrop: #3c4246;
    --brand-red: #d92328;
    --brand-grey: #77787a;
    --ink: #1e1e1e;
    --paper: #ffffff;
  }
  html, body {
    margin: 0;
    width: 1200px;
    height: 1000px;
    overflow: hidden;
    background: var(--backdrop);
    font-family: "Mulish", "Helvetica Neue", Arial, sans-serif;
  }
  .canvas { position: relative; width: 1200px; height: 1000px; }

  .card { position: absolute; overflow: hidden; box-shadow: 0 10px 24px rgba(0,0,0,.45); }

  .card--back {
    left: 117px; top: 86px; width: 711px; height: 390px;
    background: var(--brand-red);
    display: flex; align-items: center; justify-content: center;
  }
  .back-wordmark {
    color: var(--paper);
    font-weight: 800;
    font-size: 34px;
    letter-spacing: 2px;
    text-transform: uppercase;
    text-align: center;
    line-height: 1.15;
  }

  .card--front {
    left: 378px; top: 528px; width: 719px; height: 390px;
    background: var(--paper);
  }
  .front-curves { position: absolute; inset: 0; }

  .front-brand {
    position: absolute; left: 52px; top: 100px; width: 240px;
    display: flex; flex-direction: column; align-items: center;
  }
  .brand-dot {
    width: 84px; height: 84px; border-radius: 50%;
    background: var(--brand-red);
    margin-bottom: 26px;
  }
  .brand-name {
    color: var(--brand-red);
    font-weight: 800;
    font-size: 25px;
    line-height: 1.1;
    letter-spacing: 1px;
    text-transform: uppercase;
    text-align: center;
  }

  .holder-name {
    position: absolute; left: 359px; top: 44px;
    font-weight: 700; font-size: 21px; color: var(--ink);
  }
  .holder-address {
    position: absolute; left: 359px; top: 127px;
    font-size: 18px; line-height: 24px; color: var(--ink);
  }
  .contact-list {
    position: absolute; left: 354px; top: 240px;
    margin: 0; padding: 0; list-style: none;
  }
  .contact-item {
    display: flex; align-items: center; gap: 12px;
    height: 39.5px;
    font-size: 18.5px; color: var(--ink);
  }
  .contact-icon { width: 24px; height: 24px; flex: none; }
</style>
</head>
<body>
<div class="canvas">

  <section class="card card--back" aria-label="Card back">
    <div class="back-wordmark">Marrowfield<br>Contracting</div>
  </section>

  <section class="card card--front" aria-label="Card front">
    <svg class="front-curves" width="719" height="390" viewBox="0 0 719 390" aria-hidden="true">
      <path d="M590 0 L630 0 A300 300 0 0 1 719 95 L719 130 A290 290 0 0 0 590 0 Z" fill="var(--brand-grey)"/>
      <path d="M0 255 A300 300 0 0 0 130 390 L90 390 A300 300 0 0 1 0 300 Z" fill="var(--brand-red)"/>
    </svg>

    <div class="front-brand">
      <div class="brand-dot"></div>
      <div class="brand-name">Marrowfield<br>Contracting LLC</div>
    </div>

    <div class="holder-name">Name</div>
    <div class="holder-address">addresss<br>address</div>

    <ul class="contact-list">
      <li class="contact-item">
        <svg class="contact-icon" viewBox="0 0 24 24" aria-hidden="true"><path fill="var(--ink)" d="M6.6 10.8a15.2 15.2 0 0 0 6.6 6.6l2.2-2.2a1 1 0 0 1 1-.25 11.4 11.4 0 0 0 3.6.57 1 1 0 0 1 1 1V20a1 1 0 0 1-1 1A17 17 0 0 1 3 4a1 1 0 0 1 1-1h3.5a1 1 0 0 1 1 1c0 1.25.2 2.45.57 3.57a1 1 0 0 1-.25 1z"/></svg>
        000-000-0000
      </li>
      <li class="contact-item">
        <svg class="contact-icon" viewBox="0 0 24 24" aria-hidden="true"><rect x="2" y="5" width="20" height="14" fill="var(--ink)"/><path d="M2.5 5.5 12 13l9.5-7.5" stroke="#fff" stroke-width="1.6" fill="none"/></svg>
        @marrowfieldcontracting.com
      </li>
      <li class="contact-item">
        <svg class="contact-icon" viewBox="0 0 24 24" aria-hidden="true" fill="none" stroke="var(--ink)" stroke-width="1.8"><circle cx="12" cy="12" r="10"/><ellipse cx="12" cy="12" rx="4.5" ry="10"/><path d="M2 12h20M4 7h16M4 17h16"/></svg>
        www.marrowfieldcontracting.com
      </li>
    </ul>
  </section>

</div>
</body>
</html>
```